Innovative Consulting Firm Needs New Business Cards and Stationary

Our Innovative Consulting Firm, Larkfield Consulting, is in need of new business cards and stationary designs. We want two-sided cards that incorporate our logo, which is attached. We are looking for something not too formal, but is professional and slick.

Card should have the following information:
Name (ex. Tom Bradley)
Title (ex. Manager)
Address (ex. 24680 Cedar Lane)
Address 2 (ex. Suite 100)
City
State
Zip Code
Mobile
Email

The card should also have our website: www.larkfieldconsulting.example

Industry/Entity Type

Management Consulting

Contact Information for Business Card

Name (ex. Tom Bradley)
Title (ex. Manager)
Address 2 (ex. Suite 100)
City
State
Zip Code
Mobile
Email

Font styles to use
Sans Serif

Requirements
Must have
• The colors on the card must match the colors in the logo. The exact color codes are attached in a pdf.
Nice to have
• The Company's Tagline is "Focused on your Future". This might be nice to incorporate, but not necessary.

```html
<!DOCTYPE html>
<html lang="en">
<head>
<meta charset="utf-8">
<title>Larkfield Consulting – Business Cards</title>
<link href="https://fonts.googleapis.com/css2?family=Open+Sans:wght@400;600;700&display=swap" rel="stylesheet">
<style>
  :root {
    --navy: #17467a;
    --navy-deep: #123c6a;
    --gold: #e8a41c;
    --paper: #f7f7f7;
    --ink: #4a4a4a;
    --backdrop-light: #3a3a3a;
    --backdrop-dark: #151515;
  }
  * { margin: 0; padding: 0; box-sizing: border-box; }
  html, body { width: 1200px; height: 834px; overflow: hidden; }
  body {
    position: relative;
    font-family: "Open Sans", sans-serif;
    background: radial-gradient(ellipse at 50% 40%, var(--backdrop-light), var(--backdrop-dark) 75%);
  }
  .card {
    position: absolute;
    width: 520px;
    height: 297px;
    background: var(--paper);
    box-shadow: 0 10px 28px rgba(0,0,0,.55);
    overflow: hidden;
  }
  .card--front { left: 120px; top: 110px; }
  .card--back  { left: 560px; top: 420px; }

  .wordmark {
    display: flex;
    align-items: center;
    gap: 10px;
    color: var(--navy);
    font-weight: 600;
    font-size: 30px;
    letter-spacing: .5px;
    white-space: nowrap;
  }
  .wordmark__dot {
    width: 14px; height: 14px;
    border-radius: 50%;
    background: var(--gold);
  }
  .card--front .wordmark {
    position: absolute; left: 50%; top: 50%;
    transform: translate(-50%, -50%);
  }
  .card--back .wordmark {
    position: absolute; right: 34px; top: 48px;
    font-size: 26px;
  }

  .contact { position: absolute; left: 38px; top: 100px; z-index: 1; }
  .contact__name { color: var(--navy); font-weight: 700; font-size: 18px; line-height: 1.15; }
  .contact__title { color: var(--gold); font-size: 13px; line-height: 1.3; margin-bottom: 10px; }
  .contact__address { color: var(--ink); font-size: 11.5px; line-height: 1.5; margin-bottom: 5px; }
  .contact__line {
    display: flex; align-items: center; gap: 9px;
    color: var(--ink); font-size: 11.5px; line-height: 1.6;
  }
  .contact__line svg { width: 11px; height: 11px; flex: none; }

  .wave { position: absolute; left: 0; top: 0; width: 520px; height: 297px; }
</style>
</head>
<body>
  <section class="card card--front" aria-label="Card front">
    <div class="wordmark"><span class="wordmark__dot"></span>Larkfield Consulting</div>
  </section>

  <section class="card card--back" aria-label="Card back">
    <svg class="wave" viewBox="0 0 520 297" aria-hidden="true">
      <path d="M0,254 C180,254 270,236 340,186 S462,122 520,118 L520,297 L0,297Z" fill="var(--gold)"/>
      <path d="M0,261 C180,261 272,243 342,193 S464,129 520,125 L520,297 L0,297Z" fill="#ffffff"/>
      <path d="M0,264 C180,264 274,246 344,196 S466,132 520,128 L520,297 L0,297Z" fill="var(--navy-deep)"/>
    </svg>

    <div class="wordmark"><span class="wordmark__dot"></span>Larkfield Consulting</div>

    <div class="contact">
      <p class="contact__name">Tom Bradley</p>
      <p class="contact__title">Manager</p>
      <p class="contact__address">24680 Cedar Lane, Suite 11<br>Millbrook, Oregon 97201</p>
      <p class="contact__line">
        <svg viewBox="0 0 12 12" aria-hidden="true"><rect x="3" y="0.8" width="6" height="10.4" rx="1.2" fill="none" stroke="var(--gold)" stroke-width="1.2"/><circle cx="6" cy="9.3" r=".7" fill="var(--gold)"/></svg>
        (555) 014-2290
      </p>
      <p class="contact__line">
        <svg viewBox="0 0 12 12" aria-hidden="true"><rect x=".8" y="2.4" width="10.4" height="7.2" fill="none" stroke="var(--gold)" stroke-width="1.2"/><path d="M1,2.8 L6,6.8 L11,2.8" fill="none" stroke="var(--gold)" stroke-width="1.2"/></svg>
        email@larkfieldconsulting.example
      </p>
    </div>
  </section>
</body>
</html>
```